Set up small scale company website

We need a website set up for our educational consultancy - Kelvra Learning. We like the following site and want something similar www.plindaworks.co.uk We can provide the copy and images but need the following:- setting up the overall theme and design - to our requirements on colours and forma- Approximately 4 pages of services offered and with an index pageEtct (yellow and green)And the following pages - as well as a home page:- A contact page linked to our email addresses and registered business address 47 Bramwick Lane, Harwich, Essex, CO14 8RJ- About Us page - An index of services page that links to between 4-6 pages outlining services- A News page that links to updates of latest services, events and activities - easily updated by usOn the homepage we'd like links to twitter and LinkedIn feeds and links to our other blogs and websites
Target Market(s)
Schools, local authoroties and multi-academy trusts
Logo Text
Kelvra Learning
Coding
Coded - Design and coding required
Number of Pages Required
5+ page
Font styles to use
Requirements
Should not have
- No tacky pictures of mortar boards or chalk boards etc.

```html
<!DOCTYPE html>
<html lang="en">
<head>
<meta charset="utf-8">
<title>Kelvra Learning</title>
<link rel="stylesheet" href="https://fonts.googleapis.com/css2?family=Lato:wght@400;700;900&display=swap">
<style>
:root{
  --green:#6aa300;
  --green-dark:#4f8a00;
  --yellow:#e8d40c;
  --pale-yellow:#fbf6c2;
  --navy:#1c3d6e;
  --text:#4a4a4a;
  --muted:#7a7a7a;
  --bar:#efefef;
  --section:#f5f5f5;
  --white:#ffffff;
}
*{box-sizing:border-box;margin:0;padding:0}
html,body{width:1099px;height:1200px;overflow:hidden}
body{font-family:"Lato",sans-serif;color:var(--text);background:var(--white);position:relative}

.top-bar{position:absolute;left:0;top:0;width:1099px;height:45px;background:var(--bar)}
.contact-item{position:absolute;top:14px;font-size:12.5px;color:#333;display:flex;align-items:center;gap:12px;letter-spacing:.3px}
.contact-item svg{flex:none}
.contact-phone{left:105px}
.contact-mail{left:237px}
.social{position:absolute;left:868px;top:0;display:flex;height:45px}
.social-cell{width:58px;height:45px;border-left:1px solid #d6d6d6;display:flex;align-items:center;justify-content:center}
.social-cell:last-child{border-right:1px solid #d6d6d6}
.social-dot{width:14px;height:14px;border-radius:50%;background:#c9ad12}

.site-header{position:absolute;left:0;top:45px;width:1099px;height:75px;background:var(--white)}
.brand{position:absolute;left:105px;top:27px;font-size:21px;font-weight:700;color:var(--green);letter-spacing:.6px;text-transform:uppercase}
.main-nav{position:absolute;top:0;left:0;width:100%;height:75px}
.nav-link{position:absolute;top:0;height:75px;line-height:72px;font-size:12.5px;color:#111;letter-spacing:.4px;text-transform:uppercase;text-align:center}
.nav-home{left:565px;width:50px}
.nav-services{left:638px;width:92px;background:linear-gradient(180deg,#eee21a,#dcc40a)}
.nav-news{left:755px;width:50px}
.nav-about{left:845px;width:72px}
.nav-contact{left:953px;width:70px}

.hero{position:absolute;left:0;top:120px;width:1099px;height:302px;overflow:hidden}
.hero-photo{position:absolute;inset:0;background:linear-gradient(90deg,#f4f2ee 0%,#ece8e0 30%,#c9b8a6 48%,#6e5a4d 62%,#3b3436 75%,#8a6f5c 86%,#2f3a5a 100%)}
.hero-copy{position:absolute;left:103px;top:98px}
.hero-kicker{font-size:29px;font-weight:900;color:var(--green);letter-spacing:.8px;margin-left:35px;line-height:36px}
.hero-line{font-size:30px;font-weight:700;color:#8a8a8a;line-height:34px;letter-spacing:.3px}
.slider-dots{position:absolute;left:519px;top:281px;display:flex;gap:8px}
.slider-dots span{width:14px;height:7px;background:#111}
.slider-dots span.active{background:var(--yellow)}

.welcome{position:absolute;left:0;top:422px;width:1099px;height:204px}
.welcome h1{position:absolute;top:36px;width:100%;text-align:center;font-size:20px;font-weight:700;color:#4a4a4a;letter-spacing:.4px}
.welcome p{position:absolute;left:107px;top:74px;width:915px;font-size:13.2px;line-height:24px;color:#555;letter-spacing:.55px}

.services{position:absolute;left:0;top:626px;width:1099px;height:529px;background:var(--section)}
.services h2{position:absolute;top:18px;width:100%;text-align:center;font-size:21px;font-weight:700;color:#4a4a4a;letter-spacing:1.4px}
.service{position:absolute;width:262px}
.service-icon{position:absolute;top:0;width:58px;height:56px;border-radius:8px;background:linear-gradient(160deg,#8cc21a,#5d9b00)}
.service h3{position:absolute;top:66px;left:0;font-size:14.5px;font-weight:700;color:var(--navy);letter-spacing:1.2px;white-space:nowrap}
.service p{position:absolute;top:89px;left:0;width:256px;font-size:12.4px;line-height:20px;color:#555;letter-spacing:1px}
.service a{color:var(--navy);text-decoration:none}

.s1{left:105px;top:75px}.s2{left:447px;top:75px}.s3{left:792px;top:75px}
.s4{left:104px;top:304px}.s5{left:447px;top:304px}.s6{left:792px;top:304px}
.s1 .service-icon{left:78px}.s1 h3{left:78px}
.s2 .service-icon{left:96px}.s2 h3{left:90px}
.s3 .service-icon{left:97px}.s3 h3{left:92px}
.s4 .service-icon{left:80px}.s4 h3{left:45px}
.s5 .service-icon{left:99px}.s5 h3{left:77px}
.s6 .service-icon{left:103px}.s6 h3{left:93px}

.feed-band{position:absolute;left:0;top:1155px;width:1099px;height:45px;background:var(--pale-yellow)}
.feed-icons{position:absolute;left:537px;top:20px;display:flex;gap:4px;align-items:flex-end}
.feed-icons span{width:22px;height:22px;border:2px solid #555;border-radius:4px}
.feed-arrows{position:absolute;left:959px;top:21px;display:flex;gap:2px}
.feed-arrow{width:40px;height:26px;background:var(--green);display:flex;align-items:center;justify-content:center}
</style>
</head>
<body>

<div class="top-bar">
  <div class="contact-item contact-phone">
    <svg width="20" height="20" viewBox="0 0 24 24" aria-hidden="true"><path d="M6.6 10.8a15.1 15.1 0 0 0 6.6 6.6l2.2-2.2c.3-.3.7-.4 1-.2 1.1.4 2.3.6 3.6.6.6 0 1 .4 1 1V20c0 .6-.4 1-1 1A17 17 0 0 1 3 4c0-.6.4-1 1-1h3.5c.6 0 1 .4 1 1 0 1.3.2 2.5.6 3.6.1.3 0 .7-.2 1z" fill="#c9ad12"/></svg>
    <span>47 512 309</span>
  </div>
  <div class="contact-item contact-mail">
    <svg width="20" height="15" viewBox="0 0 20 15" aria-hidden="true"><rect width="20" height="15" rx="1.5" fill="#c9ad12"/><path d="M1 1.5l9 6.5 9-6.5" stroke="#fff" stroke-width="1.6" fill="none"/></svg>
    <span>hello@kelvralearning.com</span>
  </div>
  <div class="social">
    <div class="social-cell"><span class="social-dot"></span></div>
    <div class="social-cell"><span class="social-dot"></span></div>
    <div class="social-cell"><span class="social-dot"></span></div>
  </div>
</div>

<header class="site-header">
  <div class="brand">Kelvra Learning</div>
  <nav class="main-nav">
    <a class="nav-link nav-home">Home</a>
    <a class="nav-link nav-services">Services</a>
    <a class="nav-link nav-news">News</a>
    <a class="nav-link nav-about">About Us</a>
    <a class="nav-link nav-contact">Contact</a>
  </nav>
</header>

<section class="hero">
  <div class="hero-photo" role="img" aria-label="Photo of two colleagues in business suits reviewing work together"></div>
  <div class="hero-copy">
    <div class="hero-kicker">COLLABORATION</div>
    <div class="hero-line">Sharing Experience</div>
    <div class="hero-line">Resources and Opportunities</div>
  </div>
  <div class="slider-dots"><span></span><span class="active"></span><span></span><span></span></div>
</section>

<section class="welcome">
  <h1>Welcome to Kelvra Learning</h1>
  <p>Lorem ipsum dolor sit amet, consectetur adipiscing elit, sed do eiusmod tempor incididunt ut labore et dolore magna aliqua. Ut enim ad minim veniam, quis nostrud exercitation ullamco laboris nisi ut aliquip ex ea commodo consequat. Duis aute irure dolor in reprehenderit in voluptate velit esse cillum dolore eu fugiat nulla pariatur. Excepteur sint occaecat cupidatat non proident, sunt in culpa qui officia deserunt mollit anim id est laborum.</p>
</section>

<section class="services">
  <h2>Services</h2>
  <div class="service s1">
    <div class="service-icon" role="img" aria-label="Finance icon"></div>
    <h3>Finance</h3>
    <p>Lorem ipsum dolor sit amet, consecte-tur adipiscing elit, sed do eiusmod tempor incididunt ut labore et dolore magna aliqua. Ut enim ad minim veniam, <a>Read More</a></p>
  </div>
  <div class="service s2">
    <div class="service-icon" role="img" aria-label="Personnel icon"></div>
    <h3>Personnel</h3>
    <p>Lorem ipsum dolor sit amet, consecte-tur adipiscing elit, sed do eiusmod tempor incididunt ut labore et dolore magna aliqua. Ut enim ad minim veniam, <a>Read More</a></p>
  </div>
  <div class="service s3">
    <div class="service-icon" role="img" aria-label="Facilities icon"></div>
    <h3>Facilities</h3>
    <p>Lorem ipsum dolor sit amet, consecte-tur adipiscing elit, sed do eiusmod tempor incididunt ut labore et dolore magna aliqua. Ut enim ad minim veniam, <a>Read More</a></p>
  </div>
  <div class="service s4">
    <div class="service-icon" role="img" aria-label="Academy conversion icon"></div>
    <h3>Academy Conversion</h3>
    <p>Lorem ipsum dolor sit amet, consecte-tur adipiscing elit, sed do eiusmod tempor incididunt ut labore et dolore magna aliqua. Ut enim ad minim veniam, <a>Read More</a></p>
  </div>
  <div class="service s5">
    <div class="service-icon" role="img" aria-label="Staff solution icon"></div>
    <h3>Staff Solution</h3>
    <p>Lorem ipsum dolor sit amet, consecte-tur adipiscing elit, sed do eiusmod tempor incididunt ut labore et dolore magna aliqua. Ut enim ad minim veniam, <a>Read More</a></p>
  </div>
  <div class="service s6">
    <div class="service-icon" role="img" aria-label="Auditing icon"></div>
    <h3>Auditing</h3>
    <p>Lorem ipsum dolor sit amet, consecte-tur adipiscing elit, sed do eiusmod tempor incididunt ut labore et dolore magna aliqua. Ut enim ad minim veniam, <a>Read More</a></p>
  </div>
</section>

<section class="feed-band">
  <div class="feed-icons"><span></span><span></span><span></span></div>
  <div class="feed-arrows">
    <div class="feed-arrow"><svg width="12" height="18" viewBox="0 0 12 18" aria-hidden="true"><path d="M10 2L3 9l7 7" stroke="#fff" stroke-width="2.5" fill="none"/></svg></div>
    <div class="feed-arrow"><svg width="12" height="18" viewBox="0 0 12 18" aria-hidden="true"><path d="M2 2l7 7-7 7" stroke="#fff" stroke-width="2.5" fill="none"/></svg></div>
  </div>
</section>

</body>
</html>
```